BrivoMatex. Lantern for the Steady Growth. Business card

Professional business card for BrivoMatex (Lantern for the Steady Growth)
My rationale: Strategy-> Execution-> Results-> Value that lead to the BrivoMatex name: We put the Lantern for the Steady Growth.
We deliver value to our customers helping them at defining a good strategy (cyan arrow). 90% of well formulated strategies fail due to poor execution so we also consider strategical execution very important (green arrow). Due to the execution we obtain the results (blue arrow). Finally, the results provide feedback to redefine strategy, and the new strategy has to be executed and new results obtained providing new feedback and on and on. It's like a wheel that finally, must create corporate value: value for shareholders, staholders, employees, providers...-

Target Market(s)

CEOs and steering comitees , invewrnent funds

Industry/Entity Type

Business Consultant

Contact Information for Business Card

Tommaso Ferlini
CEO & Founder
tommaso.ferlini@brivomatex.example
Mobile: +34 611.205.938
www.brivomatex.example

Colors

Designer to choose colors to be used in the design.

Requirements
Nice to have
• Nice to hace the words: Strategy, execution, results
• Nice to vave the claim: Lantern for the Steady Growth
• The three colors should be shown:
• cyan for STRATEGY
• green for EXECUTION
• blue for RESULTS
Should not have
• Complete black background

```html
<!DOCTYPE html>
<html lang="en">
<head>
<meta charset="utf-8">
<title>BrivoMatex – Business Card</title>
<link rel="stylesheet" href="https://fonts.googleapis.com/css2?family=PT+Sans:wght@400;700&display=swap">
<style>
  :root {
    --navy: #1f3a8c;
    --cyan: #22a3d8;
    --green: #8cc63f;
    --white: #ffffff;
    --stage-top: #e4e6e8;
    --stage-bottom: #b9bcbf;
    --card-shadow: rgba(0, 0, 0, 0.22);
  }
  * { box-sizing: border-box; margin: 0; padding: 0; }
  html, body {
    width: 1200px;
    height: 800px;
    overflow: hidden;
  }
  body {
    position: relative;
    background: linear-gradient(160deg, var(--stage-top), var(--stage-bottom));
    font-family: "PT Sans", "Myriad Pro", sans-serif;
  }
  .card {
    position: absolute;
    width: 520px;
    height: 300px;
    background: var(--white);
    box-shadow: 0 6px 18px var(--card-shadow);
    overflow: hidden;
  }
  /* Back side */
  .card--back {
    left: 600px;
    top: 80px;
    display: flex;
    flex-direction: column;
    align-items: center;
    text-align: center;
  }
  .card--back .brand-name {
    margin-top: 86px;
    font-size: 40px;
    font-weight: 700;
    color: var(--navy);
    line-height: 1;
  }
  .pillars {
    margin-top: 16px;
    font-size: 14px;
    font-weight: 700;
    letter-spacing: 0.5px;
    text-transform: uppercase;
  }
  .pillars .strategy { color: var(--cyan); }
  .pillars .execution { color: var(--green); }
  .pillars .results { color: var(--navy); }
  .pillars .dot { color: var(--navy); margin: 0 4px; }
  .claim {
    margin-top: 34px;
    font-size: 18px;
    font-weight: 700;
    color: var(--navy);
    text-transform: uppercase;
    letter-spacing: 0.3px;
  }
  /* Front side */
  .card--front {
    left: 80px;
    top: 420px;
  }
  .card--front .brand-name {
    position: absolute;
    left: 36px;
    top: 38px;
    font-size: 40px;
    font-weight: 700;
    color: var(--navy);
    line-height: 1;
  }
  .person {
    position: absolute;
    left: 38px;
    top: 104px;
  }
  .person__name {
    font-size: 21px;
    font-weight: 700;
    color: var(--navy);
    line-height: 1.1;
  }
  .person__role {
    font-size: 16px;
    color: var(--cyan);
    line-height: 1.2;
  }
  .contacts {
    position: absolute;
    left: 36px;
    top: 160px;
    list-style: none;
    font-size: 15px;
    color: var(--navy);
  }
  .contacts li {
    display: flex;
    align-items: center;
    gap: 7px;
    line-height: 21px;
  }
  .contacts svg { flex: none; }
  .base-band {
    position: absolute;
    left: 0;
    bottom: 0;
    width: 520px;
    height: 72px;
    background: linear-gradient(180deg, var(--cyan) 0%, var(--navy) 55%);
  }
  .website {
    position: absolute;
    right: 28px;
    bottom: 16px;
    font-size: 16px;
    color: var(--white);
  }
</style>
</head>
<body>

  <section class="card card--back" aria-label="Business card, back">
    <div class="brand-name">BrivoMatex</div>
    <p class="pillars">
      <span class="strategy">Strategy</span><span class="dot">•</span><span class="execution">Execution</span><span class="dot">•</span><span class="results">Results</span>
    </p>
    <p class="claim">Lantern for the Steady Growth</p>
  </section>

  <section class="card card--front" aria-label="Business card, front">
    <div class="brand-name">BrivoMatex</div>

    <div class="person">
      <p class="person__name">Tommaso Ferlini</p>
      <p class="person__role">CEO &amp; Founder</p>
    </div>

    <ul class="contacts">
      <li>
        <svg width="12" height="16" viewBox="0 0 12 16" aria-label="Mobile">
          <rect x="1" y="1" width="10" height="14" rx="2" fill="none" stroke="var(--green)" stroke-width="1.6"/>
          <line x1="4.5" y1="12.5" x2="7.5" y2="12.5" stroke="var(--green)" stroke-width="1.4"/>
        </svg>
        <span>+34 611.205.938</span>
      </li>
      <li>
        <svg width="16" height="12" viewBox="0 0 16 12" aria-label="Email">
          <rect x="1" y="1" width="14" height="10" fill="none" stroke="var(--green)" stroke-width="1.6"/>
          <polyline points="1,1 8,7 15,1" fill="none" stroke="var(--green)" stroke-width="1.6"/>
        </svg>
        <span>tommaso.ferlini@brivomatex.example</span>
      </li>
    </ul>

    <div class="base-band" role="img" aria-label="Decorative flowing band in cyan, green and navy"></div>
    <p class="website">www.brivomatex.example</p>
  </section>

</body>
</html>
```